Velmora Water Purification

We need a website set up on a "Free account" WordPress platform. (This is the type of Wordpress site that you can sign up for and create online for free (not a server-hosted type.)
The website will be for a water purification company. They install devices in homes to purify the water for safer drinking, bathing, and cleaning.
Our logo is attached. Please keep color scheme of the website consistent with the logo.
Water Purification

```html
<!DOCTYPE html>
<html lang="en">
<head>
<meta charset="utf-8">
<title>Velmora Water Purification</title>
<link href="https://fonts.googleapis.com/css2?family=Abel&family=Arimo:ital,wght@0,400;0,700;1,400&display=swap" rel="stylesheet">
<style>
:root{
  --navy-top:#35426d;
  --navy-bottom:#212a44;
  --accent:#1b78bf;
  --ink:#2b2f3a;
  --muted:#8b929c;
  --panel:#f1f4f7;
  --section:#f0f0f0;
  --rule:#dcdcdc;
  --white:#ffffff;
}
*{box-sizing:border-box;margin:0;padding:0}
html,body{width:937px;height:1200px;overflow:hidden;background:var(--white)}
body{position:relative;font-family:"Arimo",Arial,sans-serif;color:var(--ink)}
h2,h3{font-weight:400}
.abs{position:absolute}
.header-band{left:0;top:0;width:937px;height:302px;background:linear-gradient(var(--navy-top),var(--navy-bottom))}
.nav-marker{left:456px;top:0;width:0;height:0;border-left:5px solid transparent;border-right:5px solid transparent;border-top:5px solid #3d8fe0}
.brand{left:44px;top:30px;display:flex;align-items:center;gap:7px;font-family:"Abel",sans-serif;font-size:13px;color:#dfe8f5;width:220px;line-height:1.2}
.brand-dot{width:14px;height:14px;border-radius:50%;background:#4c8fd4;flex:none}
.header-divider{left:328px;top:20px;width:1px;height:60px;background:rgba(255,255,255,.15)}
.nav{left:430px;top:22px;display:flex}
.nav-item{text-align:center;padding:0 14px;border-left:1px dotted rgba(255,255,255,.25);height:24px}
.nav-item:first-child{border-left:none}
.nav-label{font-size:8.5px;font-weight:700;color:var(--white);display:block}
.nav-sub{font-size:5.5px;font-style:italic;color:#7d89a8;display:block;margin-top:3px}
.slider{left:134px;top:91px;width:669px;height:341px;background:var(--white)}
.slide{left:138px;top:96px;width:658px;height:252px;background:radial-gradient(ellipse at 55% 40%,#7fe0ec 0%,#1d8fa8 40%,#0a4f68 100%)}
.slide-bar{left:142px;top:348px;width:654px;height:3px;background:#9fd3ee}
.intro-panel{left:138px;top:351px;width:665px;height:81px;background:var(--panel)}
.slider-arrow{top:347px;width:15px;height:15px;background:#3a3f48;color:#fff;font-size:8px;line-height:15px;text-align:center}
.intro-title{left:138px;top:377px;width:665px;text-align:center;font-family:"Abel",sans-serif;font-size:15px;color:var(--accent)}
.intro-text{left:138px;top:400px;width:665px;text-align:center;font-size:7.5px;color:var(--muted)}
.intro-text span{color:var(--accent)}
.ornament{border-radius:50%;background:radial-gradient(circle,#6fb0dc 0%,#3f83b8 45%,rgba(63,131,184,0) 72%)}
.rule{height:1px;background:var(--rule)}
.card{top:460px;width:154px;background:var(--white);box-shadow:0 0 2px rgba(0,0,0,.12)}
.card-photo{position:absolute;left:8px;top:7px;width:137px;height:118px}
.card-title{position:absolute;left:17px;top:143px;font-family:"Abel",sans-serif;font-size:11px;line-height:11px;color:var(--accent);text-transform:uppercase}
.card-rule{position:absolute;left:8px;right:8px;top:171px;height:1px;background:#e6e6e6}
.card-text{position:absolute;left:17px;right:14px;top:184px;font-size:6.6px;line-height:10px;color:#444}
.card-btn{position:absolute;left:48px;width:58px;height:18px;border:1px solid #dcdcdc;font-size:7px;line-height:16px;text-align:center;color:#555}
.to-top{left:909px;width:22px;height:22px;border-radius:50%}
.drinking{left:142px;top:770px;width:652px;height:330px;background:var(--section);border-top:4px solid #d3d3d3}
.drinking-title{left:170px;top:795px;font-family:"Abel",sans-serif;font-size:12px;color:var(--ink)}
.drinking-photo{top:831px;height:183px}
.drinking-heading{left:170px;top:1026px;font-family:"Abel",sans-serif;font-size:10.5px;color:var(--accent);letter-spacing:.2px}
.drinking-text{left:170px;top:1046px;font-family:"Abel",sans-serif;font-size:8px;color:#333;letter-spacing:.1px}
.drinking-note{left:170px;top:1068px;font-family:"Abel",sans-serif;font-size:8px;font-style:italic;color:#222}
</style>
</head>
<body>
<div class="abs header-band"></div>
<div class="abs nav-marker"></div>
<div class="abs brand"><span class="brand-dot"></span>Velmora Water Purification</div>
<div class="abs header-divider"></div>
<nav class="abs nav">
  <div class="nav-item"><span class="nav-label">HOME</span></div>
  <div class="nav-item"><span class="nav-label">ABOUT US</span><span class="nav-sub">who we are</span></div>
  <div class="nav-item"><span class="nav-label">SERVICES</span><span class="nav-sub">what we do</span></div>
  <div class="nav-item"><span class="nav-label">QUALITY</span><span class="nav-sub">our tips &amp; advice</span></div>
  <div class="nav-item"><span class="nav-label">CONTACT US</span><span class="nav-sub">location</span></div>
</nav>

<div class="abs slider"></div>
<div class="abs slide" role="img" aria-label="Underwater view of rising air bubbles in clear turquoise water"></div>
<div class="abs slide-bar"></div>
<div class="abs intro-panel"></div>
<div class="abs slider-arrow" style="left:452px">&larr;</div>
<div class="abs slider-arrow" style="left:469px">&rarr;</div>
<div class="abs intro-title">WATER IS OUR SPECIALTY!</div>
<div class="abs intro-text">We are a complete home <span>water</span> purification, filtration &amp; installation company.</div>

<div class="abs ornament" style="left:108px;top:360px;width:80px;height:80px" role="img" aria-label="Decorative water droplet with a globe inside"></div>
<div class="abs rule" style="left:142px;top:443px;width:652px"></div>

<article class="abs card" style="left:142px;height:282px">
  <div class="card-photo" role="img" aria-label="Under-sink water filtration unit installed in a home" style="background:linear-gradient(#8fa9bf,#c9d3db 55%,#6d7680)"></div>
  <h3 class="card-title">Whole Home<br>Filtration</h3>
  <div class="card-rule"></div>
  <p class="card-text">Whole home filtration is our specialty. We install systems that purify every tap for safer drinking, bathing and cleaning. Free water testing &amp; fair pricing....</p>
  <div class="card-btn" style="top:250px">read more</div>
</article>
<article class="abs card" style="left:309px;height:282px">
  <div class="card-photo" role="img" aria-label="Clean water flowing from a kitchen tap" style="background:linear-gradient(#b9d3ea,#2b7fb1 50%,#e9eef2 70%)"></div>
  <h3 class="card-title">Drinking Water<br>Systems</h3>
  <div class="card-rule"></div>
  <p class="card-text">It is important to have clean water at every glass. We guarantee our work. Reverse Osmosis, UV Units, Softeners, Residential &amp; Commercial...</p>
  <div class="card-btn" style="top:250px">read more</div>
</article>
<article class="abs card" style="left:475px;height:270px">
  <div class="card-photo" role="img" aria-label="Technician replacing a water filter cartridge" style="background:linear-gradient(#6a7a86,#a5b3bd 45%,#4f6272)"></div>
  <h3 class="card-title">Filter Service &amp;<br>Repairs</h3>
  <div class="card-rule"></div>
  <p class="card-text">Did you know that according to health guidelines, home filter cartridges should be replaced every 6 to 12 months for safe water? ...</p>
  <div class="card-btn" style="top:240px">read more</div>
</article>
<article class="abs card" style="left:642px;height:270px">
  <div class="card-photo" role="img" aria-label="Pen resting on a contract signature line" style="background:linear-gradient(135deg,#c9c9c9,#f2f2f2 60%,#dedede)"></div>
  <h3 class="card-title">Maintenance<br>Contracts</h3>
  <div class="card-rule"></div>
  <p class="card-text">We can provide Maintenance Contracts for Filters, Purifier Cleaning and Repairs for both Commercial &amp; Residential clients....</p>
  <div class="card-btn" style="top:240px">read more</div>
</article>

<div class="abs ornament" style="left:826px;top:650px;width:88px;height:88px" role="img" aria-label="Decorative water droplet with a globe inside"></div>

<svg class="abs to-top" style="top:447px" viewBox="0 0 22 22" aria-hidden="true"><circle cx="11" cy="11" r="11" fill="#b9b9b9"/><path d="M7 13 L11 9 L15 13" stroke="#fff" stroke-width="1.2" fill="none"/></svg>
<svg class="abs to-top" style="top:787px" viewBox="0 0 22 22" aria-hidden="true"><circle cx="11" cy="11" r="11" fill="#4a4d52"/><path d="M7 13 L11 9 L15 13" stroke="#fff" stroke-width="1.2" fill="none"/></svg>
<svg class="abs to-top" style="top:1161px" viewBox="0 0 22 22" aria-hidden="true"><circle cx="11" cy="11" r="11" fill="#b9b9b9"/><path d="M7 13 L11 9 L15 13" stroke="#fff" stroke-width="1.2" fill="none"/></svg>

<section class="abs drinking"></section>
<h2 class="abs drinking-title">FRESH CLEAN DRINKING WATER</h2>
<div class="abs drinking-photo" style="left:166px;width:278px;background:linear-gradient(90deg,#ffffff,#e4eefb 60%,#b7cff0)" role="img" aria-label="Saving water illustration with a glass piggy bank half filled with water"></div>
<div class="abs drinking-photo" style="left:505px;width:274px;background:linear-gradient(135deg,#1d63b8,#7fb3e6 55%,#d8e9f8)" role="img" aria-label="Water being poured from a bottle into a glass"></div>
<div class="abs drinking-heading">OVER 30 YEARS OF EXPERIENCE IN THE WATER BUSINESS.</div>
<div class="abs drinking-text">WE LOVE SERVING OUR CUSTOMERS. OUR CUSTOMERS ARE ONE OF THE REASONS WHY WE CONSTANTLY LOOK TO PROVIDE BETTER SERVICE.</div>
<div class="abs drinking-note">* PROUD MEMBERS OF THE ISLAND WATER QUALITY GUILD.</div>
<div class="abs rule" style="left:142px;top:1129px;width:652px"></div>
</body>
</html>
```